Tallowind Concrete

We are looking for a design for a two sided over-sized postcard to show the beauty of the work we provide. We want it to be simple, bold & elegant as well as eye catching. Feel free to crop the images supplied to whatever looks best.

Website is www.twq-plains.com for more information, verbiage, contact information, etc.

```html
<!DOCTYPE html>
<html lang="en">
<head>
<meta charset="utf-8">
<title>Tallowind Concrete – Postcard</title>
<link rel="stylesheet" href="https://fonts.googleapis.com/css2?family=Cinzel:wght@700&family=Open+Sans:ital,wght@0,400;0,700;0,800;1,400&display=swap">
<style>
  :root {
    --page: #e8e5e0;
    --dark: #2b231f;
    --dark-panel: rgba(38, 30, 26, 0.9);
    --green: #8cc63f;
    --white: #ffffff;
    --muted: #cfc6bd;
    --mail: #d9d6d1;
    --brick: #9a5a3a;
    --stone: #c07a48;
  }
  * { box-sizing: border-box; margin: 0; padding: 0; }
  html, body { width: 1200px; height: 900px; overflow: hidden; background: var(--page); }
  body { font-family: "Open Sans", Arial, sans-serif; position: relative; }

  .card { position: absolute; top: 250px; width: 560px; height: 400px; overflow: hidden; box-shadow: 0 2px 6px rgba(0,0,0,.18); }
  .card--back { left: 30px; background: var(--mail); }
  .card--front { left: 610px; }

  .brand { display: flex; align-items: center; gap: 8px; }
  .brand__mark { width: 22px; height: 22px; background: var(--white); flex: none; }
  .brand__name { color: var(--white); font-weight: 800; font-size: 14px; text-transform: uppercase; letter-spacing: .5px; line-height: 1; }

  /* Front */
  .front-photo { position: absolute; inset: 0; background: linear-gradient(135deg, #5a4a3e 0%, var(--brick) 30%, var(--stone) 60%, #a8643c 100%); }
  .front-panel { position: absolute; left: 0; top: 0; width: 236px; height: 336px; background: var(--dark-panel); padding: 24px 20px; }
  .headline { font-family: "Cinzel", Georgia, serif; color: var(--green); font-size: 27px; line-height: 1.05; margin-top: 22px; }
  .subhead { font-family: "Cinzel", Georgia, serif; color: var(--green); font-size: 14px; line-height: 1.2; margin-top: 4px; }
  .intro { color: var(--muted); font-size: 9.5px; line-height: 1.5; margin-top: 14px; }
  .estimate { color: var(--white); font-weight: 700; font-size: 10.5px; margin-top: 12px; }
  .front-band { position: absolute; left: 0; right: 0; bottom: 0; height: 64px; background: var(--dark); display: flex; align-items: center; justify-content: space-between; padding: 0 22px; }
  .call { font-family: "Cinzel", Georgia, serif; color: var(--green); font-size: 26px; }
  .contact { display: flex; gap: 18px; color: var(--white); font-weight: 700; font-size: 14px; }
  .contact__item { display: flex; align-items: center; gap: 6px; }
  .contact svg { width: 14px; height: 14px; }

  /* Back */
  .back-panel { position: absolute; left: 0; top: 0; width: 350px; height: 100%; background: var(--dark); padding: 18px 20px; }
  .section-title { font-family: "Cinzel", Georgia, serif; color: var(--green); font-size: 20px; letter-spacing: 1px; }
  .gallery { display: flex; gap: 6px; margin-top: 10px; }
  .gallery__tile { flex: 1; height: 62px; border: 2px solid #4a3e37; }
  .gallery__tile--a { background: linear-gradient(135deg, #7a6a5c, #b07850); }
  .gallery__tile--b { background: linear-gradient(135deg, #8a8480, #5a5450); }
  .gallery__tile--c { background: linear-gradient(135deg, #b5703e, #7c4a2e); }
  .services { list-style: none; margin-top: 12px; }
  .service { position: relative; padding-left: 14px; margin-bottom: 7px; }
  .service::before { content: ""; position: absolute; left: 0; top: 3px; border-left: 7px solid var(--green); border-top: 4px solid transparent; border-bottom: 4px solid transparent; }
  .service__name { color: var(--white); font-weight: 700; font-size: 10px; text-transform: uppercase; }
  .service__text { color: var(--muted); font-size: 8.5px; line-height: 1.35; }
  .back-footer { position: absolute; left: 20px; right: 20px; bottom: 16px; display: flex; justify-content: space-between; align-items: center; }
  .back-contact { color: var(--white); font-size: 10px; font-weight: 700; text-align: right; line-height: 1.5; }
  .mail-area { position: absolute; left: 350px; top: 0; right: 0; bottom: 0; background: linear-gradient(160deg, #e4e1dc, var(--mail)); }
</style>
</head>
<body>

<section class="card card--back" aria-label="Postcard back">
  <div class="back-panel">
    <h2 class="section-title">SERVICES</h2>
    <div class="gallery">
      <div class="gallery__tile gallery__tile--a" role="img" aria-label="Photo of a stained concrete patio"></div>
      <div class="gallery__tile gallery__tile--b" role="img" aria-label="Photo of a sealed garage floor"></div>
      <div class="gallery__tile gallery__tile--c" role="img" aria-label="Photo of a stained wooden fence"></div>
    </div>
    <ul class="services">
      <li class="service"><p class="service__name">Sealing &amp; Weatherproofing</p><p class="service__text">Protect surfaces from water, sun and stains with a lasting clear seal.</p></li>
      <li class="service"><p class="service__name">Acid Staining – Exterior</p><p class="service__text">Rich, varied colour for patios, walks and drives that never peels.</p></li>
      <li class="service"><p class="service__name">Garage Epoxy</p><p class="service__text">Durable, glossy floors that resist oil, chips and daily wear.</p></li>
      <li class="service"><p class="service__name">Deck &amp; Fence Staining &amp; Sealing</p><p class="service__text">Restore and protect wood with stains that bring back its natural grain.</p></li>
      <li class="service"><p class="service__name">Acid Staining – Interior</p><p class="service__text">Marbled, one of a kind tones for floors inside your home or office.</p></li>
    </ul>
    <div class="back-footer">
      <div class="brand"><span class="brand__mark"></span><span class="brand__name">Tallowind Concrete</span></div>
      <div class="back-contact">555-014-2867<br>www.twq-plains.com</div>
    </div>
  </div>
  <div class="mail-area"></div>
</section>

<section class="card card--front" aria-label="Postcard front">
  <div class="front-photo" role="img" aria-label="Photo of a stamped stone-pattern concrete driveway beside a brick house"></div>
  <div class="front-panel">
    <div class="brand"><span class="brand__mark"></span><span class="brand__name">Tallowind Concrete</span></div>
    <h1 class="headline">ENRICH &amp;<br>PRESERVE</h1>
    <p class="subhead">your stone,<br>concrete or wood!</p>
    <p class="intro">Tallowind Concrete is a locally owned team that restores and enhances stone, concrete and wood. We use quality materials and careful methods so every surface looks its best for years to come.</p>
    <p class="estimate">Always a FREE ESTIMATE!</p>
  </div>
  <div class="front-band">
    <span class="call">CALL NOW!</span>
    <div class="contact">
      <span class="contact__item">
        <svg viewBox="0 0 24 24" aria-hidden="true"><path fill="#fff" d="M6.6 10.8a15.1 15.1 0 0 0 6.6 6.6l2.2-2.2a1 1 0 0 1 1-.25 11.4 11.4 0 0 0 3.6.6 1 1 0 0 1 1 1V20a1 1 0 0 1-1 1A17 17 0 0 1 3 4a1 1 0 0 1 1-1h3.5a1 1 0 0 1 1 1c0 1.25.2 2.45.6 3.6a1 1 0 0 1-.25 1z"/></svg>
        555-014-2867
      </span>
      <span class="contact__item">
        <svg viewBox="0 0 24 24" aria-hidden="true"><g fill="none" stroke="#fff" stroke-width="2"><circle cx="12" cy="12" r="9"/><path d="M3 12h18M12 3c3 3.5 3 14.5 0 18M12 3c-3 3.5-3 14.5 0 18"/></g></svg>
        www.twq-plains.com
      </span>
    </div>
  </div>
</section>

</body>
</html>
```